GDFH Business Card

Looking for a business card design to incorporate our branding. We want to only use the colors listing in the Branding Package (attached).
Updates

Target Market(s)

People who need their phone or device fixed.

Industry/Entity Type

Electronics

Contact Information for Business Card

Please use:

Gadget Fix Haven LLC
4870 S Ridgecrest Pkwy
Suite 318
San Antonio, TX 78291

Wendell Thorsby, Store Manager

(210) 555-0147

Requirements
Must have
• Must include the colors that are contained within the Branding Package PDF file.

```html
<!DOCTYPE html>
<html lang="en">
<head>
<meta charset="utf-8">
<title>Gadget Fix Haven — Business Card</title>
<link rel="stylesheet" href="https://fonts.googleapis.com/css2?family=Arimo:wght@400;700&family=Archivo+Black&display=swap">
<style>
  :root {
    --backdrop: #4a4a4a;
    --card-white: #fdfaf9;
    --brand-orange: #ee5424;
    --brand-lime: #cfdc5a;
    --ink-grey: #46494c;
    --paper-white: #ffffff;
  }
  * { box-sizing: border-box; margin: 0; padding: 0; }
  html, body {
    width: 1200px; height: 800px; overflow: hidden;
    background: var(--backdrop);
  }
  .canvas { position: relative; width: 1200px; height: 800px; }
  .card {
    position: absolute; left: 338px; width: 545px; height: 320px;
    border-radius: 18px;
  }
  .card--front { top: 78px; background: var(--card-white); }
  .card--back { top: 422px; background: var(--brand-orange); color: var(--paper-white); }

  .brand {
    position: absolute; left: 60px; top: 112px;
    display: flex; align-items: center; gap: 22px;
  }
  .brand__square {
    width: 92px; height: 92px; border-radius: 12px;
    background: var(--brand-orange);
  }
  .brand__name {
    font-family: "Arimo", Arial, sans-serif; font-weight: 400;
    font-size: 42px; color: var(--brand-orange); letter-spacing: 0.2px;
  }

  .back__marker {
    position: absolute; left: 76px; top: 172px;
    width: 36px; height: 36px; border-radius: 6px;
    background: var(--brand-lime);
  }
  .contact {
    position: absolute; left: 159px; top: 42px;
    font-family: "Arimo", Arial, sans-serif;
  }
  .contact__address { font-size: 17px; line-height: 22px; font-style: normal; }
  .contact__phone {
    margin-top: 12px; font-family: "Archivo Black", Arial, sans-serif;
    font-size: 17px; letter-spacing: 0.3px;
  }
  .person { position: absolute; left: 34px; top: 238px; }
  .person__name {
    font-family: "Archivo Black", Arial, sans-serif;
    font-size: 21px; letter-spacing: 0.4px; line-height: 26px;
  }
  .person__role {
    font-family: "Arimo", Arial, sans-serif;
    font-size: 17px; letter-spacing: 0.3px; line-height: 22px;
  }
</style>
</head>
<body>
<main class="canvas">
  <section class="card card--front" aria-label="Card front">
    <div class="brand">
      <span class="brand__square" aria-hidden="true"></span>
      <span class="brand__name">Gadget Fix Haven</span>
    </div>
  </section>

  <section class="card card--back" aria-label="Card back">
    <span class="back__marker" aria-hidden="true"></span>
    <div class="contact">
      <address class="contact__address">4870 S Ridgecrest Pkwy, Suite 318<br>San Antonio, TX 78291</address>
      <p class="contact__phone">(210) 555-0147</p>
    </div>
    <div class="person">
      <p class="person__name">Wendell Thorsby</p>
      <p class="person__role">STORE MANAGER</p>
    </div>
  </section>
</main>
</body>
</html>
```